Business Card Design

We are a full service general contractor that specializes in emergency services and insurance restoration/repair. Most of our work relates to water damage, fire dame, smoke, wind and hail, storm damage, etc. Pretty much anything you would call your insurance company for.

On one side of card the logo is VERY easy with the possibility of some modifications once I get a preview. I had a logo designed years ago and its on all my vehicles so I want to stick with my branding at this point and time.

Its a 2 sided card-for one side I would like the following:
* See logo (its attached)
* I would like this logo as large/big/bold as possible-essentially it should fill up the entire side of the card (barring it not looking proportionally correct of course)
* I think the background should be white behind it-or possibly red (with colors inverted so that they don't get lost in the red background)
* I'm attaching a photo of one of our work vans to go off of-you will notice that the .com wraps up the side of the logo-this .com portion needs to added on as the logo is only the kestrel restoration logo

The other side of the card I'm thinking should be:
* My biggest struggle is formatting-in other words-I don't know how to lay out all that info without the card looking jumbled/messy
* all our logos, vehicles, marketing media, etc. is based on or at least inspired by a clean look
* a smaller version of logo (without the .com) should be located somewhere on this side of card-I've seen some cards where its centered and others where its offset-I'm not sure which is better
* I could conceivably leave off PO BOX if its too much info and something needs deleted

Business

The logo will display company name-other pertinent info:
Phone: 704 555 0182
Mobile: 704 555 0147
Fax: 704 555 0163
email: kestrelrestoration@mailnest-example.com
Address: 2958 Willow Rd.
Charlotte, NC
PO BOX 60357 28220

```html
<!DOCTYPE html>
<html lang="en">
<head>
<meta charset="utf-8">
<title>Kestrel Restoration — Business Card</title>
<link rel="stylesheet" href="https://fonts.googleapis.com/css2?family=Source+Sans+3:wght@400;700&display=swap">
<style>
  :root {
    --stage: #ececec;
    --paper: #ffffff;
    --ink-dark: #141414;
    --brand-red: #c8242b;
    --slate: #3c4a52;
    --card-shadow: rgba(0, 0, 0, 0.12);
  }
  * { box-sizing: border-box; margin: 0; padding: 0; }
  html, body {
    width: 1200px;
    height: 900px;
    overflow: hidden;
    background: var(--stage);
    font-family: "Source Sans 3", "Helvetica Neue", Arial, sans-serif;
  }
  .canvas {
    width: 1200px;
    height: 900px;
    display: flex;
    align-items: center;
    justify-content: center;
    gap: 40px;
  }
  .card {
    width: 540px;
    height: 309px;
    position: relative;
    box-shadow: 0 6px 18px var(--card-shadow);
    overflow: hidden;
  }
  .card--front { background: var(--paper); }
  .card--back {
    background: var(--ink-dark);
    display: flex;
    align-items: center;
    justify-content: center;
  }

  /* Contact block */
  .address {
    position: absolute;
    top: 30px;
    left: 36px;
    color: var(--brand-red);
    font-size: 14px;
    line-height: 1.25;
    font-style: normal;
  }
  .contact-list {
    position: absolute;
    top: 100px;
    left: 36px;
    list-style: none;
    color: var(--brand-red);
    font-size: 14px;
    line-height: 1.3;
  }
  .contact-list li {
    display: flex;
    align-items: center;
    gap: 7px;
  }
  .contact-icon { width: 11px; height: 11px; flex: none; }
  .contact-icon path, .contact-icon rect { fill: var(--slate); }

  /* Brand name block (front) */
  .brand {
    position: absolute;
    right: 38px;
    bottom: 36px;
    display: flex;
    align-items: center;
    gap: 10px;
  }
  .brand-square {
    width: 22px;
    height: 22px;
    background: var(--brand-red);
  }
  .brand-name {
    font-weight: 700;
    font-size: 30px;
    line-height: 1;
    text-transform: uppercase;
    color: var(--brand-red);
    letter-spacing: 0.01em;
  }

  /* Brand name block (back) */
  .brand-hero {
    font-weight: 700;
    font-size: 46px;
    line-height: 1.02;
    text-transform: uppercase;
    color: var(--brand-red);
    text-align: center;
    letter-spacing: 0.01em;
  }
</style>
</head>
<body>
<main class="canvas">

  <section class="card card--front" aria-label="Card front with contact details">
    <address class="address">
      2958 Willow Rd.<br>
      Charlotte, NC<br>
      PO BOX 60357 28220
    </address>

    <ul class="contact-list">
      <li>
        <svg class="contact-icon" viewBox="0 0 12 12" aria-label="Phone">
          <path d="M2.3 0.8l2 0 1 2.6-1.3 1a6 6 0 0 0 3.6 3.6l1-1.3 2.6 1 0 2a1.2 1.2 0 0 1-1.3 1.2A10 10 0 0 1 1 2.1 1.2 1.2 0 0 1 2.3 0.8z"/>
        </svg>
        704 555 0182
      </li>
      <li>
        <svg class="contact-icon" viewBox="0 0 12 12" aria-label="Mobile">
          <path d="M3 0h6a1 1 0 0 1 1 1v10a1 1 0 0 1-1 1H3a1 1 0 0 1-1-1V1a1 1 0 0 1 1-1zm0.8 1.5v7.5h4.4V1.5z"/>
        </svg>
        704 555 0147
      </li>
      <li>
        <svg class="contact-icon" viewBox="0 0 12 12" aria-label="Fax">
          <rect x="3" y="0.5" width="6" height="3.5"/>
          <path d="M1 4.5h10a1 1 0 0 1 1 1V10H9v1.5H3V10H0V5.5a1 1 0 0 1 1-1zm3 4v2h4v-2z"/>
        </svg>
        704 555 0163
      </li>
      <li class="email">kestrelrestoration@mailnest-example.com</li>
    </ul>

    <div class="brand">
      <span class="brand-square" aria-hidden="true"></span>
      <span class="brand-name">Kestrel<br>Restoration</span>
    </div>
  </section>

  <section class="card card--back" aria-label="Card back with company name">
    <p class="brand-hero">Kestrel<br>Restoration</p>
  </section>

</main>
</body>
</html>
```